Gutschein-Design für Verkauf von Online-Schmuckstücken
Zielgruppe
Wir verkaufen Online Schmuckstücke!
www.lunaring.de
Aufgabenstellung
Wir haben eine schwarze Schachtel erstellt und da drinne wird eine Geschenkgutschein sein:
Es soll sehr schlicht sein und schwarzen Hintergrund haben.
Vorderseite nur unser LOGO.
Rückseite:
Betrag: _________
Gültig Bis: _________
Code: __________
Und unten klein gedruckt steht:
Diese Karte ist gültig nur auf der online shop seite www.lunaring.de und in unserer offizielen Stores. Dieses Karte ist nicht gültig bei rabatierte Produkten und man kann nicht mit dieser karte einen Gutscheinkarte kaufen.
Der Design soll sehr schlicht und dezenz sein.

```html
<!DOCTYPE html>
<html lang="de">
<head>
<meta charset="utf-8">
<title>Lunaring Gutschein</title>
<link rel="stylesheet" href="https://fonts.googleapis.com/css2?family=Open+Sans:wght@400&display=swap">
<style>
  :root {
    --backdrop: #e4e4e4;
    --card-dark: #1e1e1e;
    --card-light: #ffffff;
    --ink: #111111;
    --silver: #9a9a9a;
    --silver-dim: #3a3a3a;
  }
  * { margin: 0; padding: 0; box-sizing: border-box; }
  html, body {
    width: 1200px;
    height: 723px;
    overflow: hidden;
    background: var(--backdrop);
    font-family: "Open Sans", sans-serif;
  }
  .voucher {
    position: absolute;
    top: 93px;
    width: 483px;
    height: 483px;
  }
  .voucher--front {
    left: 92px;
    background: var(--card-dark);
  }
  .voucher--back {
    left: 639px;
    background: var(--card-light);
    color: var(--ink);
  }
  .brand-dot {
    position: absolute;
    left: 50%;
    border-radius: 50%;
    transform: translateX(-50%);
  }
  .voucher--front .brand-dot {
    top: 184px;
    width: 64px;
    height: 64px;
    background: var(--silver-dim);
  }
  .brand-name {
    position: absolute;
    left: 0;
    right: 0;
    top: 252px;
    text-align: center;
    font-size: 34px;
    font-weight: 400;
    letter-spacing: 1px;
    color: var(--silver);
  }
  .voucher--back .brand-dot {
    top: 100px;
    width: 42px;
    height: 42px;
    background: var(--ink);
  }
  .voucher-fields {
    position: absolute;
    left: 0;
    top: 234px;
    width: 100%;
  }
  .field {
    position: relative;
    height: 32px;
  }
  .field-label {
    position: absolute;
    right: 323px;
    top: 0;
    font-size: 11px;
    line-height: 16px;
  }
  .field-line {
    position: absolute;
    left: 171px;
    top: 14px;
    width: 181px;
    height: 1px;
    background: var(--ink);
  }
  .fine-print {
    position: absolute;
    left: 0;
    right: 0;
    top: 431px;
    text-align: center;
    font-size: 7.5px;
    line-height: 10px;
  }
</style>
</head>
<body>
  <section class="voucher voucher--front">
    <div class="brand-dot"></div>
    <div class="brand-name">Lunaring</div>
  </section>

  <section class="voucher voucher--back">
    <div class="brand-dot"></div>
    <div class="voucher-fields">
      <div class="field"><span class="field-label">Betrag</span><span class="field-line"></span></div>
      <div class="field"><span class="field-label">Gültig bis</span><span class="field-line"></span></div>
      <div class="field"><span class="field-label">Code</span><span class="field-line"></span></div>
    </div>
    <p class="fine-print">
      Diese Karte ist gültig in unserem Onlineshop: www.lunaring.de und in unseren offiziellen Stores.<br>
      Dieses Karte ist nicht einzulösen bei rabattierten Produkten und beim Kauf einer Gutscheinkarte.
    </p>
  </section>
</body>
</html>
```